Halvern Drywork Business Card Design

Professional and clean design. The design colors should flow with the logo. Two-sided card with the website on the back which is:

www.HalvernDrywork.example.

"Specializing in Water Damage Restoration"

On the front I need the name, email, phone, and logo.

Name: Dorian Kettleby
Email: Dorian@HalvernDrywork.example
Phone: 555-0142-836 for now

I only have the Preview and Thumbnail right now but should have the source files uploaded within a day or two.

Target Market(s)

Flood victims, home owners with water damage from busted pipes etc...

Industry/Entity Type

Business

Contact Information for Business Card

Name: Dorian Kettleby

Font styles to use
Serif
Sans Serif

```html
<!DOCTYPE html>
<html lang="en">
<head>
<meta charset="utf-8">
<title>Halvern Drywork Business Card</title>
<link href="https://fonts.googleapis.com/css2?family=Cinzel:wght@600&family=Arimo:wght@400;700&display=swap" rel="stylesheet">
<style>
  :root {
    --brand-blue: #2a96d5;
    --brand-blue-dark: #1f86c6;
    --wave-blue: #55bdec;
    --ink-gray: #4a4a4a;
    --card-white: #ffffff;
    --backdrop: #e9ecef;
  }
  * { box-sizing: border-box; margin: 0; padding: 0; }
  html, body {
    width: 1200px; height: 950px; overflow: hidden;
    background: var(--backdrop);
    font-family: "Arimo", Arial, sans-serif;
  }
  .sheet {
    width: 1200px; height: 950px;
    display: flex; flex-direction: column;
    align-items: center; justify-content: center; gap: 30px;
  }
  .card {
    position: relative;
    width: 760px; height: 434px;
    border-radius: 4px;
    overflow: hidden;
    box-shadow: 0 6px 18px rgba(0,0,0,0.18);
  }
  /* Back side */
  .card-back { background: var(--brand-blue); color: var(--card-white); }
  .back-brand {
    position: absolute; left: 0; right: 0; top: 150px;
    display: flex; align-items: center; justify-content: center; gap: 16px;
  }
  .brand-dot {
    display: inline-block; border-radius: 50%;
  }
  .card-back .brand-dot { width: 58px; height: 58px; background: var(--card-white); }
  .back-name {
    font-family: "Cinzel", Georgia, serif; font-weight: 600;
    font-size: 34px; letter-spacing: 1px; color: var(--card-white);
  }
  .tagline {
    position: absolute; left: 0; right: 0; top: 300px;
    text-align: center; font-size: 19px; font-style: italic;
    color: var(--card-white);
  }
  /* Front side */
  .card-front { background: var(--card-white); }
  .front-brand {
    position: absolute; left: 44px; top: 50px;
    display: flex; align-items: center; gap: 12px;
  }
  .card-front .brand-dot { width: 34px; height: 34px; background: var(--brand-blue); }
  .front-name {
    font-family: "Cinzel", Georgia, serif; font-weight: 600;
    font-size: 30px; letter-spacing: 1px; color: var(--brand-blue);
  }
  .holder-name {
    position: absolute; left: 44px; top: 138px;
    font-size: 25px; font-weight: 700; color: var(--brand-blue-dark);
  }
  .contact-list {
    position: absolute; left: 44px; top: 184px;
    list-style: none; display: flex; flex-direction: column; gap: 9px;
  }
  .contact-item {
    display: flex; align-items: center; gap: 10px;
    font-size: 17px; color: var(--ink-gray);
  }
  .contact-icon { width: 16px; height: 16px; flex: none; }
  .feature-circle {
    position: absolute; left: 430px; top: 96px;
    width: 310px; height: 310px; border-radius: 50%;
    background: var(--wave-blue); opacity: 0.85;
  }
</style>
</head>
<body>
<main class="sheet">
  <section class="card card-back" aria-label="Card back">
    <div class="back-brand">
      <span class="brand-dot"></span>
      <span class="back-name">Halvern Drywork</span>
    </div>
    <p class="tagline">Specializing in Water Damage Restoration</p>
  </section>

  <section class="card card-front" aria-label="Card front">
    <div class="front-brand">
      <span class="brand-dot"></span>
      <span class="front-name">HALVERN DRYWORK</span>
    </div>
    <p class="holder-name">Dorian Kettleby</p>
    <ul class="contact-list">
      <li class="contact-item">
        <svg class="contact-icon" viewBox="0 0 16 16" aria-hidden="true"><path fill="#2a96d5" d="M3.6 1.2l2.3 2.6-1.2 1.9c.9 2 2.6 3.7 4.6 4.6l1.9-1.2 2.6 2.3-1.3 2.4C7.3 13.6 2.4 8.7 1.2 3z"/></svg>
        <span>555-0142-836 for now</span>
      </li>
      <li class="contact-item">
        <svg class="contact-icon" viewBox="0 0 16 16" aria-hidden="true"><rect x="1" y="3" width="14" height="10" rx="1" fill="#2a96d5"/><path d="M1.5 3.8L8 9l6.5-5.2" stroke="#fff" stroke-width="1.3" fill="none"/></svg>
        <span>Dorian@HalvernDrywork.example</span>
      </li>
      <li class="contact-item">
        <svg class="contact-icon" viewBox="0 0 16 16" aria-hidden="true"><path fill="#2a96d5" d="M8 1a5 5 0 0 0-5 5c0 3.6 5 9 5 9s5-5.4 5-9a5 5 0 0 0-5-5zm0 7a2 2 0 1 1 0-4 2 2 0 0 1 0 4z"/></svg>
        <span>www.HalvernDrywork.example</span>
      </li>
    </ul>
    <div class="feature-circle" aria-hidden="true"></div>
  </section>
</main>
</body>
</html>
```